Vodka Bottle Label - Lumo Vodka

I need a bottle label for a vodka I'd like to make called Lumo Vodka.
I would like a label that looks elegant and fresh. I would like some mountains and colours to be red and white. Open to other colours being added but not too colourful. "Lumo" means fresh, dawn in polish, i would like if mountains or something extra was added to the label too. I would like the Lumo Vodka name not to be too small.
The vodka is made in australia and is 37%.

I would love to have a little bit of gold colour in the label!

I will provide the back label words when completing my decision.

i'd like to make it more simple and less european looking. More australian.

I saw a bottle like this and i did like the concept.

https://www.peltonbrewhall.com.au/spirits/zorn-vodka-range?srsltid=QxTmWiikdhaRr52-gf-k7w31ndQjvpy_mH4LtZbBEXsdp9rPeLnuVxsm

Target Market(s)

Vodka Drinkers

Industry/Entity Type

Alcohol

Colors
EB3D1F
EC4F4E
F09395
F8D3D4
FCEDEE

Requirements
Must have
• red and white colours incorporated, mountains or freshness on it.
Nice to have
• Fresh and clean look. Classy

```html
<!DOCTYPE html>
<html lang="en">
<head>
<meta charset="utf-8">
<title>Lumo Vodka – Bottle Label</title>
<link rel="stylesheet" href="https://fonts.googleapis.com/css2?family=Montserrat:wght@400;500;600;700&display=swap">
<style>
  :root {
    --backdrop: #cfcfcf;
    --night: #2a0a10;
    --wine: #5a1a24;
    --rose-deep: #a83d4a;
    --rose: #c0535a;
    --brand-red: #b0374a;
    --white: #ffffff;
    --gold-light: #f6e3a2;
    --gold: #ebc63f;
    --gold-deep: #e6b52f;
    --pink: #eba5a4;
    --pink-soft: #fbd0cb;
    --ink-dark: #3a1014;
    --leaf: #8cbf3f;
    --sky-top: #de7a6c;
    --sky-mid: #c9575b;
    --ridge: #5a1f2b;
  }
  * { margin: 0; padding: 0; box-sizing: border-box; }
  html, body {
    width: 1200px; height: 3088px; overflow: hidden;
    background: var(--backdrop);
    font-family: "Montserrat", sans-serif;
  }
  .label {
    position: absolute; left: 90px; top: 126px;
    width: 1020px; height: 2836px;
    overflow: hidden;
    background: linear-gradient(180deg, var(--night) 680px, var(--wine) 1000px, var(--rose-deep) 1350px, var(--rose) 1784px);
  }
  .landscape {
    position: absolute; left: 0; top: 0; width: 1020px; height: 680px;
    background: linear-gradient(180deg, var(--sky-top) 0%, #e08c7c 30%, var(--sky-mid) 55%, #8e3a4a 80%, var(--ridge) 100%);
  }
  .frond {
    position: absolute;
    background: radial-gradient(ellipse at center, rgba(140,191,63,0.85) 0%, rgba(140,191,63,0.35) 55%, rgba(140,191,63,0) 72%);
  }
  .frond--top { left: 60px; top: 830px; width: 244px; height: 230px; }
  .frond--bottom { left: 780px; top: 1340px; width: 200px; height: 270px; }
  .brand {
    position: absolute; left: 0; width: 100%;
    text-align: center; color: var(--white);
    font-weight: 700; line-height: 1; letter-spacing: 2px;
  }
  .brand__line { display: block; font-size: 200px; }
  .brand__line--first { position: absolute; top: 1000px; left: 0; width: 100%; padding-left: 10px; }
  .brand__line--second { position: absolute; top: 1240px; left: 0; width: 100%; padding-left: 20px; }
  .origin {
    position: absolute; top: 1690px; left: 0; width: 100%;
    text-align: center; color: var(--white);
    font-size: 56px; font-weight: 500;
  }
  .info {
    position: absolute; left: 0; top: 1784px; width: 1020px; height: 552px;
    background: linear-gradient(90deg, var(--gold-light), var(--gold) 60%, var(--gold-deep));
  }
  .info__band {
    position: absolute; left: 0; width: 1020px; height: 80px;
    display: flex; align-items: center; justify-content: center;
    color: var(--brand-red); font-weight: 600; font-size: 54px; letter-spacing: 18px;
  }
  .info__band--top { top: 0; }
  .info__band--bottom { top: 466px; height: 86px; }
  .info__panel {
    position: absolute; left: 0; top: 80px; width: 1008px; height: 386px;
    background: var(--white);
  }
  .info__headline {
    height: 196px; display: flex; align-items: center; justify-content: center;
    color: var(--brand-red); font-weight: 600; font-size: 64px;
  }
  .info__row {
    margin-left: 14px; height: 86px;
    border-top: 5px solid var(--brand-red); border-bottom: 5px solid var(--brand-red);
    display: flex; align-items: center; justify-content: center;
    color: var(--brand-red); font-weight: 600; font-size: 54px; letter-spacing: 16px;
  }
  .info__cells { display: flex; height: 104px; margin-left: 14px; }
  .info__cell {
    flex: none; display: flex; align-items: center; justify-content: center;
    color: var(--brand-red); font-size: 38px; font-weight: 500;
  }
  .info__cell + .info__cell { border-left: 5px solid var(--brand-red); }
  .info__cell:nth-child(1) { width: 340px; }
  .info__cell:nth-child(2) { width: 316px; }
  .info__cell:nth-child(3) { width: 338px; }
  .strip-pink {
    position: absolute; left: 0; top: 2336px; width: 1020px; height: 140px;
    background: linear-gradient(180deg, #e89a9a, #f0aca9);
  }
  .strength {
    position: absolute; left: 0; top: 2476px; width: 1020px; height: 250px;
    background: linear-gradient(90deg, var(--gold-light), var(--gold) 60%, var(--gold-deep));
    color: var(--ink-dark); text-align: center;
  }
  .strength__name { position: absolute; top: 70px; width: 100%; font-size: 34px; font-weight: 500; }
  .strength__abv { position: absolute; top: 128px; width: 100%; font-size: 58px; font-weight: 600; letter-spacing: 16px; }
  .strength__abv b { font-weight: 700; }
  .strip-blush {
    position: absolute; left: 0; top: 2726px; width: 1020px; height: 110px;
    background: linear-gradient(180deg, #fbc6c0, var(--pink-soft));
  }
</style>
</head>
<body>
  <main class="label">
    <div class="landscape" role="img" aria-label="Illustrated dawn landscape with sun, birds, layered red mountains and pine trees"></div>
    <div class="frond frond--top" role="img" aria-label="Green palm frond"></div>
    <div class="frond frond--bottom" role="img" aria-label="Green palm frond"></div>
    <h1 class="brand">
      <span class="brand__line brand__line--first">LUMO</span>
      <span class="brand__line brand__line--second">VODKA</span>
    </h1>
    <p class="origin">The vodka is made in australia</p>
    <section class="info">
      <div class="info__band info__band--top">DUMY TEXT IS HERE</div>
      <div class="info__panel">
        <div class="info__headline">DUMMY TEXT IS HERE</div>
        <div class="info__row">DUMMY TEXT IS HERE</div>
        <div class="info__cells">
          <div class="info__cell">Dumy text</div>
          <div class="info__cell">Dumy text</div>
          <div class="info__cell">Dumy text</div>
        </div>
      </div>
      <div class="info__band info__band--bottom">DUMY TEXT IS HERE</div>
    </section>
    <div class="strip-pink"></div>
    <section class="strength">
      <p class="strength__name">LUMO VODKA</p>
      <p class="strength__abv">The vodka is <b>37%</b></p>
    </section>
    <div class="strip-blush"></div>
  </main>
</body>
</html>
```